Thornbury Cleaning – Website Redesign (Clean, Modern, Trust-Focused)

Thornbury Cleaning — Homepage Redesign Brief

Project Goal

We need a complete redesign of the homepage for our cleaning business, Thornbury Cleaning.
The goal is a clean, modern, trust-building homepage that works equally well for:
• Residential clients
• Commercial clients

The page should feel polished, reliable, easy to navigate, and completely free from clutter, gimmicks, or corporate-sounding fluff.

About Us (Context)

Thornbury Cleaning has operated in Sale, Victoria for over 30 years.
Our brand is built on:
• Reliability
• Convenience
• Long-term trust
• Straightforward, no-nonsense communication

We do not want to look like a large franchise, and we do not want to look cute or playful.
The design must feel modern, practical, confident, and professional.

What We Need Designed — Homepage Only

1. Hero Section

A clean, modern hero area with:
• A simple image or clean background (no clutter, no heavy overlays).
Images from our current site may be helpful, or you may source alternatives.
• Headline suggestion (designer may refine):
“30+ Years of Commercial and Residential Cleaning in Sale”
• Sub-headline suggestion:
“Trusted by locals for three decades.”
• Primary CTA button: Get a Quote

2. Trust-Building Logos

Positioned directly beneath the hero:
• Small, neat logos of organisations we work with
(RLK, Bramwell, Eastvale Regional Care, OPM, etc.)
• A clean Reviewfind Reviews block (stars + review count)
• Must be compact, tidy, evenly spaced — not loud or oversized

3. Trust Block / Problem–Solution Copy

This section introduces why hiring cleaners can be stressful and why reliability matters.

Headline example:
“Call the cleaners you can count on.”

We have existing copy for this section.
Please present it in a minimal, breathable, modern layout that is easy to scan.

4. Stats / Counters Section

Three sharp, structured stat boxes:
• 92+ Recurring Clients
• 4,150+ Visits Per Year
• 265+ Pre-Sale / Exit Cleans

These should look clean and understated — not oversized or gimmicky.

5. Values Section

A short section featuring our core values:
• Be Real
• Do It Right
• Have Fun
• Make It Easy

Designer has flexibility with layout.
(Sections 5 and 6 may swap depending on what flows better.)

6. Services Preview

A simple grid or row with links to our main services:
• Commercial Cleaning
• Residential Cleaning
• Window Cleaning
• Steam Cleaning

Small icons or photos are fine — but no clip art or cartoon-style graphics.

7. Footer

A very clean, simple footer with contact details.
No clutter, no heavy visual styling.

Style Requirements

Overall Tone
• Clean
• Modern
• Minimal
• Trust-driven
• Easy to read and navigate

Do NOT use
• Clip art
• Cute or playful icons
• Flowers, sparkles, “feminine” cleaning imagery
• Heavy or overly bold corporate fonts
• Busy backgrounds
• Long paragraphs of text

Reference Material

Current Website (for copy + structure only)

https://thornburycleaning-example.com.au

Rough Canva Mock-Up (layout inspiration only)

(We will upload this separately. It’s not a final design — just a loose concept for spacing/flow.)

Logo

Please use the new Thornbury Cleaning logo (uploaded in files) or a placeholder if needed. Attached is a potential for a new logo or site colours not wedded to the idea though.

What the Homepage Should Communicate

Within seconds, a visitor should understand that:
• We are established
• We are local
• We are reliable
• We make cleaning easy
• Getting a quote is quick and simple

The homepage should feel effortless, trustworthy, and modern.

Deliverable

A complete homepage design layout suitable for WordPress.
Figma, Adobe XD, or a similar design tool is fine.

Target Market(s)

Residential and commercial clients in Sale, Victoria and surrounding Gippsland region. Typical clients include busy households, office managers, receptionists, medical centres, community organisations, local businesses, and real estate/property professionals. Clients value reliability, simplicity, and stress-free long-term cleaning support.

Industry/Entity Type

Cleaning services (Residential & Commercial)

Font styles to use
Sans Serif

Requirements
Must have
• • Clean, modern, minimal layout • A trust-driven design that highlights proof (logos, stats, reviews) near the top • Clear hierarchy and no clutter • A strong hero section with simple messaging and a clear CTA • Trust logos + Reviewfind Reviews block directly under the hero • Structured stats/counters section • Values section (Be Real, Do It Right, Have Fun, Make It Easy) • Services preview (Commercial, Residential, Window, Steam/Carpet) • Clean footer with contact details • Use our new Thornbury Cleaning logo (or placeholder if needed) • Easy-to-read typography and spacing • Must feel like a local, real cleaning business — not a franchise
Nice to have
• • An option with centred hero text and an option with left-aligned text • Option to preview hero section with or without a quote form • Subtle use of the navy + gold palette (not heavy or corporate) • Soft, minimal background images (not busy city skylines) • Subtle section dividers or whitespace breaks to improve flow • Slightly rounded card corners for a friendly but still modern feel
Should not have
• • No clip-art, cartoon mops, sparkles, bubbles, or generic cleaning icons • No overly bold, blocky, or corporate fonts • No “mega-city” skylines (we are a regional/rural business) • No heavy overlays, dark gradients, or cluttered hero images • No long paragraphs or dense text blocks • No template-style designs that look generic or AI-generated • No overly feminine, overly masculine, or overly playful designs • No neon colors or high-saturation palettes

```html
<!DOCTYPE html>
<html lang="en">
<head>
<meta charset="utf-8">
<title>Thornbury Cleaning – Homepage</title>
<link rel="stylesheet" href="https://fonts.googleapis.com/css2?family=Poppins:wght@400;500;600;700&display=swap">
<style>
:root{
  --navy:#13294b;
  --navy-deep:#0f2140;
  --gold:#a2843f;
  --gold-light:#c9a95c;
  --ink:#1d2433;
  --muted:#5e6675;
  --grey-bg:#f1f1f1;
  --line:#e3e5ea;
  --white:#ffffff;
}
*{box-sizing:border-box;margin:0;padding:0}
html,body{width:1200px;height:4708px;overflow:hidden}
body{font-family:"Poppins",sans-serif;color:var(--ink);background:var(--white);position:relative}
.abs{position:absolute}
.btn{display:inline-flex;align-items:center;gap:10px;background:var(--gold);color:var(--white);font-size:13px;font-weight:600;letter-spacing:.5px;text-transform:uppercase;padding:0 22px;height:44px;border-radius:3px;text-decoration:none}
.btn svg{width:16px;height:16px}
.brand{font-family:"Poppins",sans-serif;font-weight:700;font-size:22px;letter-spacing:1px;text-transform:uppercase;line-height:1.05;color:var(--navy)}

/* header */
.site-header{left:0;top:0;width:1200px;height:92px;background:var(--white);display:flex;align-items:center;padding:0 80px;justify-content:space-between;z-index:3}
.main-nav{display:flex;gap:30px;font-size:15px;font-weight:500;color:var(--navy);margin-left:-120px}
.header-contact{height:44px;padding:0 32px}

/* hero */
.hero{left:0;top:92px;width:1200px;height:770px;overflow:hidden}
.hero-photo{position:absolute;inset:0;background:linear-gradient(100deg,#2d3641 0%,#55606b 30%,#a8a39c 60%,#d8d2c8 100%)}
.hero-copy{position:absolute;left:80px;top:100px;width:520px;color:var(--white)}
.hero-copy h1{font-size:50px;font-weight:700;line-height:1.18}
.hero-copy p{font-size:19px;margin:18px 0 34px}
.hero-badge{position:absolute;right:80px;top:95px;width:150px;height:150px;border-radius:50%;background:var(--white);border:6px solid var(--navy)}
.hero-curve{left:0;top:780px;width:1200px;height:90px;z-index:2}
.hero-chevron{left:570px;top:825px;width:60px;height:60px;border-radius:50%;background:var(--white);box-shadow:0 4px 14px rgba(0,0,0,.15);display:flex;align-items:center;justify-content:center;z-index:3}

/* partners */
.partners{left:116px;top:866px;width:968px;display:flex;gap:22px}
.partner{flex:1;height:84px;background:#f4f5f7;border:1px solid var(--line);display:flex;align-items:center;justify-content:center;font-size:22px;font-weight:600;color:var(--navy);text-align:center;line-height:1.1}
.rating{left:490px;top:980px;width:220px;height:56px;border-radius:28px;background:var(--white);box-shadow:0 3px 14px rgba(0,0,0,.1);display:flex;align-items:center;justify-content:center;gap:10px;font-size:13px;color:var(--muted)}
.rating .dot{width:24px;height:24px;border-radius:50%;background:var(--navy)}
.rating b{font-size:18px;color:var(--ink)}
.stars{color:#f2b21c;letter-spacing:1px}

/* reviews */
.reviews{left:80px;top:1064px;width:1040px;height:300px}
.review-card{position:absolute;top:0;width:300px;height:290px;background:var(--white);border-radius:6px;box-shadow:0 4px 18px rgba(0,0,0,.08);padding:50px 26px 0}
.review-card .quote{position:absolute;right:26px;top:14px;font-size:56px;color:var(--gold);font-weight:700;line-height:1}
.review-card p{font-size:12.5px;line-height:1.65;color:var(--muted)}
.review-card .who{position:absolute;left:26px;right:26px;bottom:22px;display:flex;justify-content:space-between;align-items:flex-end}
.review-card .who strong{font-size:12px;font-weight:600;display:block;color:var(--ink)}
.review-card .who .mark{width:20px;height:20px;border-radius:50%;background:var(--line)}
.slider-arrow{position:absolute;top:130px;width:34px;height:34px;border-radius:50%;display:flex;align-items:center;justify-content:center}
.dots{left:580px;top:1384px;display:flex;gap:6px}
.dots i{width:7px;height:7px;border-radius:50%;background:#c8ccd4}
.dots i:first-child{background:var(--navy)}

/* about */
.about{left:0;top:1490px;width:1200px;height:630px;background:var(--grey-bg)}
.about-frame{left:88px;top:1594px;width:440px;height:414px;border:3px solid var(--gold)}
.about-photo{left:108px;top:1574px;width:440px;height:414px;background:linear-gradient(135deg,#cfd3d6,#8a96a3 55%,#2d4a6d)}
.about-copy{left:620px;top:1588px;width:480px}
.about-copy h2{font-size:34px;font-weight:600;line-height:1.2;color:var(--navy)}
.about-copy p{font-size:13.5px;line-height:1.7;color:var(--muted);margin-top:16px}
.about-copy .btn{margin-top:22px;height:48px}

/* stats */
.stats{left:80px;top:2192px;width:1040px;display:flex;gap:40px}
.stat{flex:1;height:168px;background:var(--white);border-radius:6px;box-shadow:0 4px 22px rgba(0,0,0,.08);display:flex;align-items:center;gap:22px;padding-left:48px}
.stat-icon{width:52px;height:52px;display:flex;align-items:center;justify-content:center}
.stat b{display:block;font-size:38px;font-weight:600;color:var(--gold);line-height:1}
.stat span{font-size:13px;color:var(--muted)}

/* values */
.values{left:0;top:2426px;width:1200px;height:660px}
.values-title{left:0;top:2516px;width:1200px;text-align:center;font-size:36px;font-weight:600;color:var(--white)}
.values-hub{left:472px;top:2626px;width:256px;height:256px;border-radius:50%;border:1px dashed rgba(255,255,255,.5);display:flex;align-items:center;justify-content:center}
.values-hub .brand{color:var(--white);text-align:center;font-size:24px}
.value{position:absolute;width:320px;color:var(--white);display:flex;align-items:center;gap:18px}
.value.left{flex-direction:row-reverse;text-align:right}
.value h3{font-size:20px;font-weight:600}
.value p{font-size:13px;line-height:1.55;color:#c7cfdc}
.value-icon{flex:none;width:64px;height:64px;border-radius:50%;background:var(--gold);display:flex;align-items:center;justify-content:center}
.values-cta{left:507px;top:2918px;height:48px}

/* services */
.services-title{left:0;top:3148px;width:1200px;text-align:center;font-size:36px;font-weight:600;color:var(--navy)}
.service{position:absolute;width:476px;border-radius:6px;overflow:hidden}
.service .photo{position:absolute;inset:0}
.service .label{position:absolute;left:28px;bottom:28px;color:var(--white);font-size:20px;font-weight:600;text-shadow:0 1px 6px rgba(0,0,0,.35)}

/* footer */
.footer-curve{left:0;top:4128px;width:1200px;height:80px}
.footer{left:0;top:4190px;width:1200px;height:518px;background:var(--navy-deep);color:var(--white)}
.footer-brand{left:80px;top:4290px}
.footer-brand .brand{color:var(--white)}
.socials{left:80px;top:4360px;display:flex;gap:12px}
.socials i{width:38px;height:38px;border-radius:50%;background:var(--gold)}
.socials i+i{background:transparent;border:1px solid rgba(255,255,255,.5)}
.footer-col{position:absolute;top:4214px}
.footer-col h4{font-size:20px;font-weight:600;margin-bottom:18px}
.footer-col li{list-style:none;font-size:14px;color:#d3d9e4;margin-bottom:14px;display:flex;gap:12px;align-items:flex-start;line-height:1.5}
.footer-col li svg{flex:none;width:18px;height:18px;margin-top:2px}
.copyright{left:80px;top:4656px;font-size:13px;color:#d3d9e4}
.payments{left:918px;top:4650px;display:flex;gap:8px}
.payments i{width:42px;height:26px;border-radius:3px;background:#e9ecf1}
</style>
</head>
<body>

<header class="site-header abs">
  <div class="brand">Thornbury<br>Cleaning</div>
  <nav class="main-nav"><span>Home</span><span>Commercial</span><span>Residential</span><span>Window Cleaning</span><span>Steam Cleaning</span></nav>
  <a class="btn header-contact">Contact</a>
</header>

<section class="hero abs">
  <div class="hero-photo" role="img" aria-label="Cleaners in blue uniforms vacuuming a sofa and a living room floor"></div>
  <div class="hero-copy">
    <h1>30+ Years of Commercial &amp; Residential Cleaning in Sale</h1>
    <p>Trusted by locals for three decades.</p>
    <a class="btn">Get a Quote <svg viewBox="0 0 16 16"><path d="M2 8h11M9 4l4 4-4 4" stroke="#fff" stroke-width="1.8" fill="none"/></svg></a>
  </div>
  <div class="hero-badge" role="img" aria-label="30 years anniversary badge"></div>
</section>
<svg class="hero-curve abs" viewBox="0 0 1200 90" preserveAspectRatio="none"><path d="M0 40 Q600 110 1200 40 L1200 90 L0 90Z" fill="#fff"/><path d="M0 40 Q600 110 1200 40" stroke="#a2843f" stroke-width="4" fill="none"/></svg>
<div class="hero-chevron abs"><svg width="20" height="20" viewBox="0 0 20 20"><path d="M4 7l6 6 6-6" stroke="#13294b" stroke-width="2.2" fill="none"/></svg></div>

<div class="partners abs">
  <div class="partner">RLK</div>
  <div class="partner">Bramwell</div>
  <div class="partner" style="font-size:17px">Eastvale<br>Regional Care</div>
  <div class="partner">OPM</div>
  <div class="partner">Bramwell</div>
</div>

<div class="rating abs"><i class="dot"></i><b>4.9</b><span class="stars">★★★★★</span><span>135 Reviews</span></div>

<section class="reviews abs">
  <div class="review-card" style="left:40px"><span class="quote">“</span><p>“Ut enim ad minim veniam quis nostrud exercitation ullamco laboris commodo consequat. Duis aut reprehenderit in voluptate velit esse cillum dolore eu fugiat nulla pariatur.”</p><div class="who"><div><strong>PETER VANLO</strong><span class="stars">★★★★★</span></div><i class="mark"></i></div></div>
  <div class="review-card" style="left:370px"><span class="quote">“</span><p>“Ut enim ad minim veniam quis nostrud exercitation ullamco laboris commodo consequat. Duis aut reprehenderit in voluptate velit esse cillum dolore eu fugiat nulla pariatur.”</p><div class="who"><div><strong>PETER VANLO</strong><span class="stars">★★★★★</span></div><i class="mark"></i></div></div>
  <div class="review-card" style="left:700px"><span class="quote">“</span><p>“Ut enim ad minim veniam quis nostrud exercitation ullamco laboris commodo consequat. Duis aut reprehenderit in voluptate velit esse cillum dolore eu fugiat nulla pariatur.”</p><div class="who"><div><strong>PETER VANLO</strong><span class="stars">★★★★★</span></div><i class="mark"></i></div></div>
  <div class="slider-arrow" style="left:-54px;background:#e3e5ea"><svg width="14" height="14" viewBox="0 0 14 14"><path d="M9 2L4 7l5 5" stroke="#13294b" stroke-width="2" fill="none"/></svg></div>
  <div class="slider-arrow" style="left:1060px;background:var(--navy)"><svg width="14" height="14" viewBox="0 0 14 14"><path d="M5 2l5 5-5 5" stroke="#fff" stroke-width="2" fill="none"/></svg></div>
</section>
<div class="dots abs"><i></i><i></i><i></i><i></i></div>

<section class="about abs"></section>
<div class="about-frame abs"></div>
<div class="about-photo abs" role="img" aria-label="Two cleaners mopping and vacuuming a living room"></div>
<div class="about-copy abs">
  <h2>Call the Cleaners You<br>Can Count On</h2>
  <p>When you need help cleaning, the last thing you want is more stress. Too often, that's exactly what happens —</p>
  <p>Cleaners don't show up. Jobs get rushed or half done. And you're left wondering why you didn't just do it yourself. You shouldn't have to second-guess whether the job will be done right. You should be able to book it, forget it, and trust it's sorted properly.</p>
  <p>Trusted by locals for 30+ years to deliver reliable, long term cleaning — the kind you never have to second-guess.</p>
  <a class="btn">Learn More <svg viewBox="0 0 16 16"><path d="M2 8h11M9 4l4 4-4 4" stroke="#fff" stroke-width="1.8" fill="none"/></svg></a>
</div>

<section class="stats abs">
  <div class="stat"><div class="stat-icon"><svg width="40" height="34" viewBox="0 0 40 34"><circle cx="20" cy="9" r="6" fill="#13294b"/><path d="M8 32c0-8 5-13 12-13s12 5 12 13z" fill="#13294b"/><circle cx="7" cy="12" r="4" fill="#13294b"/><circle cx="33" cy="12" r="4" fill="#13294b"/></svg></div><div><b>92+</b><span>Recurring Clients</span></div></div>
  <div class="stat"><div class="stat-icon"><svg width="36" height="36" viewBox="0 0 36 36"><rect x="3" y="6" width="30" height="27" rx="3" fill="#13294b"/><rect x="7" y="14" width="22" height="15" fill="#fff"/><rect x="9" y="2" width="3" height="8" fill="#13294b"/><rect x="24" y="2" width="3" height="8" fill="#13294b"/></svg></div><div><b>4,150+</b><span>Visits Per Year</span></div></div>
  <div class="stat"><div class="stat-icon"><svg width="30" height="40" viewBox="0 0 30 40"><rect x="6" y="14" width="18" height="24" rx="3" fill="#13294b"/><rect x="10" y="6" width="10" height="8" fill="#13294b"/><rect x="10" y="2" width="16" height="4" fill="#13294b"/></svg></div><div><b>265+</b><span>Pre-Sale / Exit Cleans</span></div></div>
</section>

<svg class="values abs" viewBox="0 0 1200 660" preserveAspectRatio="none"><path d="M0 14 Q600 -14 1200 14 L1200 660 L0 660Z" fill="#13294b"/></svg>
<h2 class="values-title abs">Our Core Values</h2>
<div class="values-hub abs"><svg class="abs" style="left:-1px;top:-1px" width="256" height="256" viewBox="0 0 256 256"><circle cx="128" cy="128" r="96" stroke="rgba(255,255,255,.85)" stroke-width="1.5" fill="none"/></svg><div class="brand">Thornbury<br>Cleaning</div></div>

<div class="value left" style="left:140px;top:2632px"><div class="value-icon"><svg width="28" height="28" viewBox="0 0 28 28"><path d="M14 24S3 17 3 10a5.5 5.5 0 0 1 11-1 5.5 5.5 0 0 1 11 1c0 7-11 14-11 14z" fill="#fff"/></svg></div><div><h3>Be Real</h3><p>Lorem ipsum dolor sit amet<br>consectetur adipiscing elit sed</p></div></div>
<div class="value left" style="left:140px;top:2762px"><div class="value-icon"><svg width="28" height="28" viewBox="0 0 28 28"><path d="M6 14l5 5 11-11" stroke="#fff" stroke-width="3" fill="none"/></svg></div><div><h3>Do It Right</h3><p>Lorem ipsum dolor sit amet<br>consectetur adipiscing elit sed</p></div></div>
<div class="value" style="left:774px;top:2632px"><div class="value-icon"><svg width="28" height="28" viewBox="0 0 28 28"><circle cx="14" cy="14" r="10" stroke="#fff" stroke-width="2.4" fill="none"/><path d="M9 16q5 5 10 0" stroke="#fff" stroke-width="2.4" fill="none"/></svg></div><div><h3>Have Fun</h3><p>Lorem ipsum dolor sit amet<br>consectetur adipiscing elit sed</p></div></div>
<div class="value" style="left:774px;top:2762px"><div class="value-icon"><svg width="28" height="28" viewBox="0 0 28 28"><path d="M4 14h20M16 6l8 8-8 8" stroke="#fff" stroke-width="3" fill="none"/></svg></div><div><h3>Make It Easy</h3><p>Lorem ipsum dolor sit amet<br>consectetur adipiscing elit sed</p></div></div>
<a class="btn values-cta abs">Get a Quote <svg viewBox="0 0 16 16"><path d="M2 8h11M9 4l4 4-4 4" stroke="#fff" stroke-width="1.8" fill="none"/></svg></a>

<h2 class="services-title abs">Our Services</h2>
<div class="service" style="left:112px;top:3256px;height:352px"><div class="photo" role="img" aria-label="Carpet being cleaned with a professional extraction wand" style="background:linear-gradient(160deg,#4e8aa0,#1e4e63 60%,#12293a)"></div><span class="label">Commercial Cleaning</span></div>
<div class="service" style="left:612px;top:3256px;height:352px"><div class="photo" role="img" aria-label="Cleaner dusting shelves in a bright home" style="background:linear-gradient(160deg,#e8e4de,#b9aea3 60%,#5d5248)"></div><span class="label">Residential Cleaning</span></div>
<div class="service" style="left:112px;top:3630px;height:372px"><div class="photo" role="img" aria-label="Cleaner in yellow gloves wiping a window" style="background:linear-gradient(160deg,#eef2f4,#a7b6c0 55%,#3f4f5c)"></div><span class="label">Window Cleaning</span></div>
<div class="service" style="left:612px;top:3630px;height:372px"><div class="photo" role="img" aria-label="Cleaner steam cleaning a floor" style="background:linear-gradient(160deg,#e6e1d8,#9d8f80 55%,#3a3430)"></div><span class="label">Steam Cleaning</span></div>

<svg class="footer-curve abs" viewBox="0 0 1200 80" preserveAspectRatio="none"><path d="M0 40 Q600 -30 1200 40 L1200 80 L0 80Z" fill="#0f2140"/><path d="M0 40 Q600 -30 1200 40" stroke="#a2843f" stroke-width="5" fill="none"/></svg>
<footer class="footer abs"></footer>
<div class="footer-brand abs"><div class="brand">Thornbury<br>Cleaning</div></div>
<div class="socials abs"><i></i><i></i><i></i></div>

<div class="footer-col" style="left:348px"><h4>Quick Links</h4><ul><li>Home</li><li>Commercial</li><li>Residential</li><li>Window Cleaning</li><li>Steam Cleaning</li></ul></div>
<div class="footer-col" style="left:584px"><h4>Services</h4><ul><li>Commercial Cleaning</li><li>Residential Cleaning</li><li>Window Cleaning</li><li>Steam Cleaning</li><li>Contact Us</li></ul></div>
<div class="footer-col" style="left:852px;width:290px"><h4>Contact Details</h4><ul>
  <li><svg viewBox="0 0 18 18"><path d="M9 1a6 6 0 0 0-6 6c0 5 6 10 6 10s6-5 6-10a6 6 0 0 0-6-6z" fill="#a2843f"/><circle cx="9" cy="7" r="2" fill="#0f2140"/></svg>27 Wattle Street Sale<br>Victoria 3850</li>
  <li><svg viewBox="0 0 18 18"><path d="M4 1l3 4-2 2q2 4 6 6l2-2 4 3-2 3Q6 16 1 3z" fill="#a2843f"/></svg>0400 000 123</li>
  <li><svg viewBox="0 0 18 18"><rect x="1" y="3" width="16" height="12" rx="1" fill="#a2843f"/><path d="M1 4l8 6 8-6" stroke="#0f2140" stroke-width="1.5" fill="none"/></svg>info@thornburycleaning-example.com.au</li>
  <li><svg viewBox="0 0 18 18"><circle cx="9" cy="9" r="8" fill="#a2843f"/><path d="M9 4v5l3 2" stroke="#0f2140" stroke-width="1.6" fill="none"/></svg>Monday – Friday 9am – 5pm</li>
</ul></div>

<p class="copyright abs">© 2025 Thornbury Cleaning</p>
<div class="payments abs"><i></i><i></i><i></i><i></i><i></i></div>

</body>
</html>
```